Kelvora Ledger Web Design Contest

We would like for you to design a website for www.kelvoraledger-example.com. Kelvora Ledger is a CPA Firm offering accounting, auditing, and tax preparation services.

We would like to have a consistent feel with the logo, business card, envelope, and stationary designs that were created by another designer on PlanHive. Examples of each are attached. We would like the website to have a clean/modern style.

The website should include the following:

1. A general "Welcome" landing page
2. A "About the Company" page
3. A "Services Offered" page
4. A "Contact Us" form
5. A button for "Sign up for Newsletter"

Target Market(s)

Individuals and businesses that require accounting, auditing, and tax preparation services from a CPA.

Industry/Entity Type

Accounting

Coding

Number of Pages Required

5+ page

Font styles to use
Other font styles liked:
• Trebuchet or similar

Requirements
Must have
• Consistent feel with logo and letterhead. The gray and blue bar on the letterhead should be incorporated into the website design.

```html
<!DOCTYPE html>
<html lang="en">
<head>
<meta charset="utf-8">
<title>Kelvora Ledger, LLC</title>
<link rel="stylesheet" href="https://fonts.googleapis.com/css2?family=Ubuntu:wght@400;500;700&family=Roboto:wght@400;500&display=swap">
<style>
:root{
  --navy:#0b2a7e;
  --navy-deep:#08205f;
  --charcoal:#4a4a4a;
  --dark-btn:#2e2e2e;
  --text:#4f4f4f;
  --light:#f0f0f0;
  --footer:#e5e5e5;
  --white:#ffffff;
}
*{margin:0;padding:0;box-sizing:border-box}
html,body{width:858px;height:1200px;overflow:hidden;background:var(--white)}
body{position:relative;font-family:"Roboto",sans-serif;color:var(--text)}
.abs{position:absolute}
.brand-bar{position:absolute;left:0;width:858px;height:17px}
.brand-bar .blue{position:absolute;left:0;top:0;height:100%;width:420px;background:var(--navy);clip-path:polygon(0 0,100% 0,98% 100%,0 100%)}
.brand-bar .gray{position:absolute;right:0;top:0;height:100%;width:446px;background:var(--charcoal);clip-path:polygon(1.5% 0,100% 0,100% 100%,0 100%)}
.top-bar{top:6px}
.bottom-bar{top:1165px;height:24px}

.logo{position:absolute;left:54px;top:29px;width:170px;text-align:center}
.logo .mark{display:block;width:38px;height:38px;border:3px solid var(--charcoal);margin:0 auto 6px}
.logo .name{font-family:"Ubuntu",sans-serif;font-size:11.5px;color:var(--navy);letter-spacing:.3px;display:block}
.logo .tagline{font-family:"Ubuntu",sans-serif;font-size:6.5px;color:#333;letter-spacing:.6px;border-top:1px solid #333;display:inline-block;padding-top:1px;margin-top:2px}

.phone{position:absolute;right:52px;top:38px;display:flex;align-items:center;gap:8px;font-family:"Ubuntu",sans-serif;font-size:16px;color:var(--navy);letter-spacing:.5px}
.nav{position:absolute;right:52px;top:72px;display:flex;align-items:center;height:25px;font-family:"Ubuntu",sans-serif;font-size:10px;color:#333}
.nav a{color:inherit;text-decoration:none;padding:0 14px;line-height:25px}
.nav a.active{background:var(--navy);color:var(--white);clip-path:polygon(10% 0,100% 0,90% 100%,0 100%);padding:0 22px;margin-right:0}

.hero{position:absolute;left:0;top:105px;width:858px;height:331px;background:linear-gradient(120deg,#3a3a3a 0%,#6d6a66 30%,#c9d3e2 55%,#e8eef7 75%,#9fb7dc 100%)}
.hero-dots{position:absolute;left:396px;top:409px;display:flex;gap:7px}
.hero-dots span{width:10px;height:10px;border-radius:50%;background:#2a2a2a}
.hero-dots span.on{background:var(--navy)}

.newsletter{position:absolute;left:0;top:436px;width:858px;height:74px;background:linear-gradient(180deg,#0b2a86 0%,#0a2a7a 70%,#0b2e88 100%)}
.newsletter h3{position:absolute;left:108px;top:27px;font-family:"Ubuntu",sans-serif;font-weight:400;font-size:16px;color:var(--white);letter-spacing:.3px}
.newsletter .field{position:absolute;left:320px;top:20px;width:302px;height:34px;background:var(--white);font-size:8px;color:#555;line-height:34px;padding-left:13px}
.newsletter .signup{position:absolute;left:636px;top:20px;width:114px;height:34px;background:linear-gradient(180deg,#fafafa,#dcdcdc);clip-path:polygon(5% 0,100% 0,95% 100%,0 100%);font-family:"Ubuntu",sans-serif;font-weight:500;font-size:11.5px;color:var(--navy);text-align:center;line-height:34px;letter-spacing:.5px}

.accent{position:absolute;height:7px;display:flex}
.accent .b{background:var(--navy);clip-path:polygon(0 0,100% 0,calc(100% - 5px) 100%,0 100%)}
.accent .g{background:#2f2f2f;clip-path:polygon(5px 0,100% 0,100% 100%,0 100%);margin-left:-3px}

.section-title{font-family:"Ubuntu",sans-serif;font-weight:400;font-size:16px;color:var(--navy);letter-spacing:.3px}

.card{position:absolute;top:608px;width:236px;height:227px;background:var(--light);text-align:center}
.card .icon{width:77px;height:77px;border-radius:50%;background:var(--navy);margin:14px auto 0;display:flex;align-items:center;justify-content:center}
.card h4{font-family:"Ubuntu",sans-serif;font-weight:500;font-size:13px;color:var(--navy);margin-top:11px;letter-spacing:.4px}
.card p{font-size:9.6px;line-height:16px;margin:5px 18px 0;color:var(--text)}
.btn{display:inline-block;background:var(--dark-btn);color:var(--white);font-family:"Ubuntu",sans-serif;font-weight:500;font-size:9.5px;letter-spacing:.3px;line-height:26px;width:79px;text-align:center;border-radius:2px}
.card .btn{margin-top:12px}

.welcome{position:absolute;left:54px;top:862px;width:360px}
.welcome p{font-size:9.8px;line-height:18.4px;margin-top:11px}
.welcome .btn{margin-top:17px}
.divider{position:absolute;left:430px;top:864px;width:1px;height:162px;background:#d6d6d6}

.news{position:absolute;left:460px;top:862px;width:350px}
.news-item{position:absolute;left:0;width:350px}
.news-item .thumb{position:absolute;left:1px;top:0;width:70px;height:56px}
.news-item .date{position:absolute;left:87px;top:-1px;font-family:"Ubuntu",sans-serif;font-weight:500;font-size:9.5px;color:var(--navy);letter-spacing:.3px}
.news-item p{position:absolute;left:87px;top:13px;width:265px;font-size:9.6px;line-height:16.3px}
.news-item p a{color:var(--navy);text-decoration:none}

.footer{position:absolute;left:0;top:1056px;width:858px;height:109px;background:var(--footer)}
.footer .links{position:absolute;left:54px;top:22px;font-size:9.6px;color:#333}
.footer .links span{margin:0 9px;color:#555}
.footer .legal{position:absolute;left:54px;top:63px;font-size:8.2px;line-height:16px;color:#555;letter-spacing:.2px}
.footer .follow{position:absolute;left:697px;top:22px;font-family:"Ubuntu",sans-serif;font-size:9.6px;color:var(--navy)}
.footer .social{position:absolute;left:697px;top:43px;display:flex;gap:7px}
.footer .social span{width:22px;height:22px;border-radius:50%;background:#2f5aa4}
.footer .social span.feed{background:#f08a1c}
</style>
</head>
<body>

<div class="brand-bar top-bar"><div class="blue"></div><div class="gray"></div></div>

<div class="logo">
  <span class="mark"></span>
  <span class="name">KELVORA LEDGER, LLC</span>
  <span class="tagline">Accounting · Audit · Tax Services</span>
</div>

<div class="phone">
  <svg width="14" height="14" viewBox="0 0 14 14"><rect width="14" height="14" rx="2" fill="#0b2a7e"/><path d="M4.2 3.2c.4-.3.9-.2 1.1.2l.7 1.3c.2.4.1.8-.2 1l-.5.4c.4.9 1.1 1.7 2 2.2l.4-.5c.3-.3.7-.4 1-.2l1.3.7c.4.2.5.7.2 1.1l-.5.7c-.4.5-1.1.6-1.7.3C5.9 9.6 4.4 8.1 3.6 6.1c-.3-.6-.2-1.3.3-1.7z" fill="#fff"/></svg>
  555 014 2290
</div>

<nav class="nav">
  <a class="active">HOME</a>
  <a>ABOUT US</a>
  <a>SERVICES</a>
  <a style="padding-right:0">CONTACT US</a>
</nav>

<div class="hero" role="img" aria-label="Photo of reading glasses resting on a financial earnings report with blue bar charts and a pen"></div>
<div class="hero-dots"><span class="on"></span><span></span><span></span><span></span></div>

<section class="newsletter">
  <h3>SIGNUP FOR NEWSLETTER</h3>
  <div class="field">Enter Email Address</div>
  <div class="signup">SIGN UP</div>
</section>

<div class="accent" style="left:356px;top:548px"><div class="b" style="width:76px"></div><div class="g" style="width:74px"></div></div>
<h2 class="section-title abs" style="left:0;width:858px;text-align:center;top:566px">OUR SERVICES</h2>

<div class="card" style="left:54px">
  <div class="icon">
    <svg width="32" height="42" viewBox="0 0 32 42"><rect x="1.5" y="1.5" width="29" height="39" rx="2" fill="none" stroke="#fff" stroke-width="3"/><rect x="6" y="6" width="20" height="7" fill="#fff"/><g fill="#fff"><rect x="6" y="17" width="5" height="4"/><rect x="13.5" y="17" width="5" height="4"/><rect x="21" y="17" width="5" height="4"/><rect x="6" y="24" width="5" height="4"/><rect x="13.5" y="24" width="5" height="4"/><rect x="21" y="24" width="5" height="4"/><rect x="6" y="31" width="5" height="4"/><rect x="13.5" y="31" width="5" height="4"/><rect x="21" y="31" width="5" height="4"/></g></svg>
  </div>
  <h4>ACCOUNTING</h4>
  <p>Aliquam molestie, mi et imperdiet euismod, dui purus auctor tellus, et interdum lacus lectus et ante.</p>
  <span class="btn">READ MORE</span>
</div>

<div class="card" style="left:311px">
  <div class="icon">
    <svg width="40" height="42" viewBox="0 0 40 42"><path d="M3 3h22l5 5v31H3z" fill="none" stroke="#fff" stroke-width="2.5"/><g stroke="#fff" stroke-width="2"><line x1="7" y1="12" x2="18" y2="12"/><line x1="7" y1="18" x2="18" y2="18"/><line x1="7" y1="24" x2="18" y2="24"/><line x1="7" y1="30" x2="18" y2="30"/></g><g fill="none" stroke="#fff" stroke-width="1.8"><path d="M20 11l2 2 3-4"/><path d="M20 17l2 2 3-4"/><path d="M20 23l2 2 3-4"/></g><rect x="33" y="8" width="4" height="24" fill="#fff"/><path d="M33 32h4l-2 5z" fill="#fff"/></svg>
  </div>
  <h4>AUDITING</h4>
  <p>Aliquam molestie, mi et imperdiet euismod, dui purus auctor tellus, et interdum lacus lectus et ante.</p>
  <span class="btn">READ MORE</span>
</div>

<div class="card" style="left:570px">
  <div class="icon">
    <svg width="46" height="34" viewBox="0 0 46 34"><rect x="1.5" y="1.5" width="34" height="31" rx="3" fill="none" stroke="#fff" stroke-width="2.5"/><rect x="35" y="5" width="9" height="26" rx="2" fill="none" stroke="#fff" stroke-width="2.2"/><rect x="6" y="5" width="23" height="11" fill="none" stroke="#fff" stroke-width="1.6"/><text x="17.5" y="14" text-anchor="middle" font-family="Ubuntu,sans-serif" font-weight="700" font-size="9" fill="#fff">TAX</text><g stroke="#fff" stroke-width="2"><line x1="6" y1="21" x2="30" y2="21"/><line x1="6" y1="26" x2="30" y2="26"/><line x1="38" y1="11" x2="41" y2="11"/><line x1="38" y1="17" x2="41" y2="17"/><line x1="38" y1="23" x2="41" y2="23"/></g></svg>
  </div>
  <h4>TAX PREPARATION</h4>
  <p>Aliquam molestie, mi et imperdiet euismod, dui purus auctor tellus, et interdum lacus lectus et ante.</p>
  <span class="btn">READ MORE</span>
</div>

<section class="welcome">
  <h2 class="section-title">WELCOME TO OUR WEBSITE</h2>
  <p>Aliquam molestie, mi et imperdiet euismod, dui purus auctor tellus, et interdum lacus lectus et ante. Sed accumsan sollicitudin sapien, sit amet adipiscing turpis gravida ac. In congue, neque ac lobortis volutpat, libero mauris varius mi, vitae suscipit ipsum ligula vitae risus. Duis aliquam nibh a dui iaculis viverra id a velit.</p>
  <span class="btn">READ MORE</span>
</section>
<div class="accent" style="left:287px;top:868px"><div class="b" style="width:65px"></div><div class="g" style="width:65px"></div></div>

<div class="divider"></div>

<section class="news">
  <h2 class="section-title">LATEST NEWS</h2>
  <div class="news-item" style="top:39px">
    <div class="thumb" role="img" aria-label="Photo of hands using a tablet and pen over paperwork" style="background:linear-gradient(135deg,#dfe6ee,#9fb0c4 60%,#e9edf2)"></div>
    <span class="date">NOV 10, 2015</span>
    <p>Sed accumsan sollicitudin sapien, sit amet adipiscing turpis gravida ac. In congue, neque ac lobortis volutpat, libero mauris varius mi...<a>Read More</a></p>
  </div>
  <div class="news-item" style="top:113px">
    <div class="thumb" role="img" aria-label="Photo of colleagues reviewing documents at an office desk" style="background:linear-gradient(135deg,#b9c7d8,#6f85a3 55%,#d8dee6)"></div>
    <span class="date">NOV 10, 2015</span>
    <p>Sed accumsan sollicitudin sapien, sit amet adipiscing turpis gravida ac. In congue, neque ac lobortis volutpat, libero mauris varius mi...<a>Read More</a></p>
  </div>
</section>
<div class="accent" style="left:588px;top:868px"><div class="b" style="width:65px"></div><div class="g" style="width:64px"></div></div>

<footer class="footer">
  <div class="links">Home<span>/</span>About us<span>/</span>Services<span>/</span>Contact us</div>
  <div class="legal">Copyright © 2015. Company Name All Right Reserved<br>Terms of Services &nbsp;|&nbsp; Privacy Policy</div>
  <div class="follow">FOLLOW US</div>
  <div class="social">
    <span aria-label="Social link 1"></span>
    <span aria-label="Social link 2" style="background:#1e8fd6"></span>
    <span aria-label="Social link 3" style="background:#1f7ab8"></span>
    <span class="feed" aria-label="News feed"></span>
  </div>
</footer>

<div class="brand-bar bottom-bar"><div class="blue"></div><div class="gray"></div></div>

</body>
</html>
```